B2B EDM Banner Design- Specialist Tech Company

We need a new top-of-email banner for our EDM campaigns for Varnel Brix (www.varnelbrix-example.com
). This banner will sit at the top of every email and must immediately signal the brand, look modern and professional, and be visually aligned with the tech/IT audience.
Size of the banner: Around 728x90 - it must fit at the top of an email blast.
Purpose of the Banner
Establish a strong, recognizable brand identity across all Varnel Brix EDMs
visually consistent with existing banners created for other brands (see reference examples provided)
Communicate Varnel Brix’s value proposition at a glance
Brand Name
Varnel Brix
Tagline (must appear in the banner)
“11,322 whitepapers from 726 companies”
Design Requirements
Style & Tone
Modern, clean, and professional
Tech-centric look and feel
High-quality, sleek, and corporate
Eye-catching but not cluttered
Should feel premium and authoritative
Layout & Composition
Full-width banner for email header
Horizontal orientation similar to the Plomtar and Quindle Staff Archive examples
Include space for the brand name/logo prominently on the left or centered
Integrate the tagline in a readable, secondary position
Optional: a subtle background texture or tech-related abstract pattern (circuitry, network nodes, gradient, etc.)
No busy imagery—should feel clean and trustworthy
Color Palette
Use colors consistent with Varnel Brix branding from www.varnelbrix-example.com
Blues, greys, blacks, and tech-style gradients preferred
Should feel consistent with a B2B IT audience
Typography
Clean, sans-serif fonts (professional/tech-aligned)
Brand name should be bold and prominent
Tagline should be smaller, but still readable on desktop and mobile
Imagery (if used)
Abstract tech shapes, network visuals, geometric patterns, or gradient overlays
Avoid photography of people
Keep imagery subtle so text remains legible
Call-to-Action Button (optional)
None required in this banner (unlike the HR examples)
Banner should remain a pure brand header
Deliverables
Final banner in PNG and JPG formats
2–3 design variations (if possible) for A/B testing
Dimensions optimized for EDM: ~600–700px wide (standard email width), proportionate height

```html
<!DOCTYPE html>
<html lang="en">
<head>
<meta charset="utf-8">
<title>Varnel Brix — EDM Header Banners</title>
<link rel="stylesheet" href="https://fonts.googleapis.com/css2?family=Montserrat:wght@500;600;800&display=swap">
<style>
  :root {
    --page: #ffffff;
    --navy-deep: #0a1c3c;
    --navy-mid: #123a6e;
    --navy-glow: #2a5f9c;
    --ice: #a8d9f2;
    --grey-band: #cfcfcf;
    --grey-light: #e4e4e4;
    --indigo: #2b3690;
    --night: #121212;
    --teal: #5cc4cb;
    --teal-dim: #2f7f8a;
    --white: #ffffff;
  }
  * { margin: 0; padding: 0; box-sizing: border-box; }
  html, body {
    width: 1200px; height: 927px; overflow: hidden;
    background: var(--page);
    font-family: "Montserrat", Arial, sans-serif;
  }
  .banner {
    position: absolute; left: 144px; width: 900px; height: 240px; overflow: hidden;
  }
  .banner__art { position: absolute; }
  .brand { font-weight: 800; letter-spacing: -1px; line-height: 1; white-space: nowrap; }
  .tagline { font-weight: 600; line-height: 1.3; white-space: nowrap; }

  /* Variation A — navy circuit */
  .banner--navy {
    top: 50px;
    background: radial-gradient(ellipse 55% 80% at 50% 45%, var(--navy-glow) 0%, var(--navy-mid) 45%, var(--navy-deep) 100%);
  }
  .banner--navy .banner__art--left {
    left: 0; top: 60px; width: 300px; height: 150px;
    background: linear-gradient(90deg, rgba(120,200,235,0.18), rgba(120,200,235,0));
  }
  .banner--navy .banner__art--right {
    right: 0; top: 20px; width: 330px; height: 200px;
    background: linear-gradient(270deg, rgba(120,200,235,0.18), rgba(120,200,235,0));
  }
  .banner--navy .banner__text { position: absolute; inset: 0; text-align: center; }
  .banner--navy .brand {
    position: absolute; left: 0; right: 0; top: 78px;
    font-size: 56px; color: var(--white);
    text-shadow: 0 0 14px rgba(160,210,255,0.7);
  }
  .banner--navy .tagline {
    position: absolute; left: 0; right: 0; top: 148px;
    font-size: 23px; color: var(--ice);
  }

  /* Variation B — grey network */
  .banner--grey { top: 338px; background: var(--grey-band); }
  .banner--grey .banner__art--right {
    right: 0; top: 0; width: 440px; height: 240px;
    background: radial-gradient(ellipse 70% 70% at 55% 55%, rgba(255,255,255,0.75), rgba(255,255,255,0.15) 70%, rgba(255,255,255,0));
  }
  .banner--grey .brand {
    position: absolute; left: 40px; top: 64px;
    font-size: 60px; color: var(--indigo);
  }
  .banner--grey .tagline {
    position: absolute; left: 40px; top: 132px;
    font-size: 25px; font-weight: 500; color: var(--indigo);
  }
  .banner--grey .tagline strong { font-weight: 800; }

  /* Variation C — black light streaks */
  .banner--night { top: 627px; background: var(--night); }
  .banner--night .banner__art--left {
    left: 0; top: 0; width: 470px; height: 240px;
    background: linear-gradient(90deg, rgba(92,196,203,0.28), rgba(92,196,203,0.08) 70%, rgba(92,196,203,0));
  }
  .banner--night .banner__text {
    position: absolute; left: 450px; width: 430px; top: 62px; text-align: center;
  }
  .banner--night .brand { font-size: 54px; color: var(--teal); }
  .banner--night .tagline {
    margin-top: 22px; font-size: 23px; font-weight: 500; color: var(--white); white-space: normal;
  }
  .banner--night .tagline strong { color: var(--teal); font-weight: 700; }
</style>
</head>
<body>

  <section class="banner banner--navy" aria-label="Variation A, navy">
    <div class="banner__art banner__art--left" role="img" aria-label="Glowing circuit-trace lines in light blue"></div>
    <div class="banner__art banner__art--right" role="img" aria-label="Glowing circuit-trace lines and dot grid in light blue"></div>
    <div class="banner__text">
      <h1 class="brand">VARNEL BRIX</h1>
      <p class="tagline">11,322 whitepapers from 726 companies</p>
    </div>
  </section>

  <section class="banner banner--grey" aria-label="Variation B, grey">
    <div class="banner__art banner__art--right" role="img" aria-label="White network of nodes joined by thin lines over faint hexagons"></div>
    <h1 class="brand">VARNEL BRIX</h1>
    <p class="tagline"><strong>11,322</strong> whitepapers from <strong>726</strong> companies</p>
  </section>

  <section class="banner banner--night" aria-label="Variation C, black">
    <div class="banner__art banner__art--left" role="img" aria-label="Horizontal teal and white light streaks fading to the right"></div>
    <div class="banner__text">
      <h1 class="brand">VARNEL BRIX</h1>
      <p class="tagline"><strong>11,322</strong> whitepapers from <strong>726</strong><br>companies</p>
    </div>
  </section>

</body>
</html>
```